Hoods and pressure washing

We pressure wash house, driveways, buisnesses, gas stations, restraunt hoods and equipments, fences, construction sites and anything that can be pressure washed
Updates

Will like my flyer to have written: licenesed, bonded, and insured up to 2 million.(but professionally written)

Target Market(s)

Restraunts, corporations, houses and apartment complexes

Industry/Entity Type

Construction

Colors
33a6d7
33b8a4
ffffff
3176b5

Requirements
Must have
• Before and after pics of dirty and clean pics
Nice to have
• I would like it to be a one paper flyer could be front or back. Company name is brightRinse. I like a corner written down with all the work we do. Ex: hoods, sidewalks, sidings, houses etc...
• Contact info: Dwayne Kellerby, phone# 629-200-5137
• Ned Loruso, phone # (didnt get one yet)
• Adress: 2487 E. Marrowfield rd, portland, Tn, 37152

```html
<!DOCTYPE html>
<html lang="en">
<head>
<meta charset="utf-8">
<title>brightRinse – Pressure Washing Flyer</title>
<link href="https://fonts.googleapis.com/css2?family=Montserrat:wght@500;600;700&display=swap" rel="stylesheet">
<style>
  :root {
    --sky: #33a6d7;
    --royal: #3176b5;
    --white: #ffffff;
    --ink: #111318;
    --backdrop: #e6e6e4;
    --grime: #5a4d42;
    --stone: #d8cdbd;
  }
  * { margin: 0; padding: 0; box-sizing: border-box; }
  html, body { width: 1200px; height: 1200px; overflow: hidden; }
  body {
    background: var(--backdrop);
    font-family: "Montserrat", sans-serif;
    color: var(--white);
  }
  .flyer {
    position: absolute;
    left: 280px; top: 120px;
    width: 640px; height: 960px;
    background: var(--sky);
    overflow: hidden;
  }
  .photo-before, .photo-after {
    position: absolute; top: 0; height: 500px;
  }
  .photo-before {
    left: 0; width: 330px;
    background: linear-gradient(180deg, #7b6d61 0%, var(--grime) 55%, #3e342d 100%);
  }
  .photo-after {
    left: 330px; width: 310px;
    background: linear-gradient(180deg, #e4dccf 0%, var(--stone) 60%, #c3b6a4 100%);
  }
  .bands { position: absolute; left: 0; top: 0; width: 640px; height: 960px; }
  .ribbon {
    position: absolute; left: 60px; top: 32px;
    width: 540px; height: 84px;
    background: var(--royal);
    transform: rotate(2deg);
    display: flex; align-items: center; justify-content: center;
  }
  .brand-name {
    font-size: 56px; font-weight: 700; letter-spacing: 2px;
    text-transform: uppercase;
  }
  .tagline {
    position: absolute; left: 195px; top: 122px;
    padding: 4px 12px;
    background: var(--sky);
    font-size: 18px; font-weight: 600; letter-spacing: 0.5px;
    transform: rotate(2deg);
  }
  .photo-label {
    position: absolute; font-size: 30px; font-weight: 700;
    text-shadow: 2px 3px 0 #222, 0 0 6px rgba(0,0,0,.6);
  }
  .label-before { left: 60px; top: 330px; transform: rotate(4deg); }
  .label-after { left: 390px; top: 398px; transform: rotate(4deg); }
  .mascot-badge {
    position: absolute; left: 36px; top: 400px;
    width: 140px; height: 150px;
  }
  .content {
    position: absolute; left: 0; top: 560px; width: 640px;
    text-align: center;
    transform: rotate(2deg);
  }
  .section-title { font-size: 30px; font-weight: 700; letter-spacing: 1px; }
  .specialities {
    margin: 14px 70px 0;
    font-size: 16px; font-weight: 500; line-height: 1.3;
    text-align: justify; text-align-last: center; hyphens: auto;
  }
  .credentials {
    margin-top: 34px; font-size: 18px; font-weight: 700; letter-spacing: 0.5px;
  }
  .block-title { margin-top: 30px; font-size: 22px; font-weight: 700; }
  .detail { font-size: 13px; font-weight: 700; letter-spacing: 0.5px; line-height: 1.45; }
</style>
</head>
<body>
  <main class="flyer">
    <div class="photo-before" role="img" aria-label="Before photo: stained, dirty building facade"></div>
    <div class="photo-after" role="img" aria-label="After photo: the same facade pressure washed clean"></div>

    <svg class="bands" viewBox="0 0 640 960" aria-hidden="true">
      <polygon points="0,430 640,470 640,960 0,960" fill="var(--sky)"/>
      <polygon points="150,420 640,450 640,500 150,470" fill="var(--royal)"/>
      <polygon points="150,470 640,500 640,512 150,480" fill="var(--ink)"/>
    </svg>

    <div class="ribbon"><span class="brand-name">brightRinse</span></div>
    <div class="tagline">PRESSURE WASHING SERVCE</div>

    <span class="photo-label label-before">BEFORE</span>
    <span class="photo-label label-after">AFTER</span>

    <svg class="mascot-badge" viewBox="0 0 140 150" role="img" aria-label="Badge illustration of a pressure washing worker">
      <polygon points="70,4 134,38 134,112 70,146 6,112 6,38" fill="var(--royal)" stroke="var(--white)" stroke-width="4"/>
      <polygon points="70,18 120,45 120,105 70,132 20,105 20,45" fill="#a9c7e4"/>
    </svg>

    <section class="content">
      <h2 class="section-title">OUR SPECIALITIES</h2>
      <p class="specialities">We specialise in pressure washing house, driveways, buisnesses, gas stations, restraunt hoods and equipments, fences, construction sites and anything that can be pressure washed</p>
      <p class="credentials">LICENESED, BONDED, AND INSURED UP TO 2 MILLION</p>
      <h3 class="block-title">-: ADDRESS :-</h3>
      <p class="detail">2487 E. MARROWFIELD RD, PORTLAND, TN, 37152</p>
      <h3 class="block-title">-: CONTACT :-</h3>
      <p class="detail">DWAYNE KELLERBY - 629-200-5137<br>NED LORUSO - 629-200-4418</p>
    </section>
  </main>
</body>
</html>
```